Packaging design (small box) for Vextra 5/6 cable (keychain cable)

we need a packaging to sell our cellphone cable.

1)I want the word "FYNE" on the life side in a stylish way...
2)The product must be mostly visible (not hidden with graphic or design)
3)Please design the sides of the packaging (colors,graphics,etc)
4)Please integrate my logo on the packaging (files 3) you can change the colour of the logo if you want.
Please check the attached files: The packaging will be exactly like this with the same material and size (file 2) (the design on the packaging of this picture is the degin by defaut from our supplier).

-They will be put in a counterdisplay

Size of the packaging:
W:36mm H:130mm D:17mm
We trust your creativity!

Attached files the sketch of our packaging and our products to inspire you.

Target Market(s)

16-35 male and female

Industry/Entity Type

Product

Requirements
Must have
• We need the following words on the packaging:
• 1)"Câble compatible pour Vextra 5/6 " (on the front)
• 2) Recharge rapidement (meaning:charge fast)
• 3) Toujours à portée de la main ( meaning always with you)
• 4)FYNE on the left side
• 5)Our logo "Marobel"
Nice to have
• I am really open about your ideas
Should not have

```html
<!DOCTYPE html>
<html lang="fr">
<head>
<meta charset="utf-8">
<title>Marobel – Vextra 5/6 keychain cable box</title>
<link href="https://fonts.googleapis.com/css2?family=Questrial&display=swap" rel="stylesheet">
<style>
  :root {
    --board: #2a2d30;
    --cut: #27b5c4;
    --paper: #ffffff;
    --magenta: #e0109a;
    --ink-light: #e6e6e6;
    --chevron-pink: #f4dfe2;
    --photo-stone: #c8bfa8;
    --swatch-orange: #f03a24;
    --swatch-pink: #d6158d;
    --swatch-green: #3dbb2a;
    --swatch-white: #ffffff;
    --swatch-black: #111214;
    --swatch-blue: #2f8be0;
  }
  html, body {
    margin: 0;
    padding: 0;
    width: 798px;
    height: 1200px;
    overflow: hidden;
    background: var(--paper);
  }
  .dieline {
    display: block;
    width: 798px;
    height: 1200px;
  }
  .panel { fill: var(--board); stroke: var(--cut); stroke-width: 2; }
  .fold { stroke: var(--cut); stroke-width: 2; fill: none; }
  .dot-white { fill: var(--paper); }
  .dot-accent { fill: var(--magenta); }
  .copy {
    font-family: "Questrial", sans-serif;
    fill: var(--ink-light);
  }
  .copy-front { font-size: 24px; }
  .copy-side { font-size: 15px; }
  .copy-tiny { font-size: 10px; }
  .brand {
    font-family: "Questrial", sans-serif;
    fill: var(--paper);
    font-size: 40px;
    letter-spacing: 6px;
  }
  .brand-band { fill: var(--board); }
  .photo-cable { fill: var(--chevron-pink); }
  .photo-keychains { fill: url(#stone); }
</style>
</head>
<body>
<svg class="dieline" viewBox="0 0 1384 2081" preserveAspectRatio="none" xmlns="http://www.w3.org/2000/svg">
  <defs>
    <linearGradient id="stone" x1="0" y1="0" x2="1" y2="1">
      <stop offset="0" stop-color="#cfc6ae"/>
      <stop offset="1" stop-color="#b9b09a"/>
    </linearGradient>
  </defs>

  <!-- left side panel with tucks -->
  <g class="side-left">
    <path class="panel" d="M25 218 V130 Q25 118 37 118 H170 Q182 118 182 130 V218 L202 272 V1808 L182 1830 V1950 Q182 1962 170 1962 H37 Q25 1962 25 1950 V1830 L0 1808 V272 L25 218 Z"/>
    <line class="fold" x1="0" y1="272" x2="202" y2="272"/>
    <line class="fold" x1="0" y1="1808" x2="202" y2="1808"/>
  </g>

  <!-- front panel with top and bottom flaps -->
  <g class="front">
    <path class="panel" d="M202 272 V30 Q202 0 232 0 H597 Q627 0 627 30 V272 Z"/>
    <line class="fold" x1="202" y1="95" x2="627" y2="95"/>
    <line class="fold" x1="290" y1="95" x2="298" y2="118"/>
    <line class="fold" x1="540" y1="95" x2="532" y2="118"/>
    <rect class="panel" x="202" y="272" width="425" height="1536"/>
    <path class="panel" d="M202 1808 H627 V2051 Q627 2081 597 2081 H232 Q202 2081 202 2051 Z"/>
    <line class="fold" x1="202" y1="1986" x2="627" y2="1986"/>
    <line class="fold" x1="290" y1="1986" x2="298" y2="1963"/>
    <line class="fold" x1="540" y1="1986" x2="532" y2="1963"/>

    <rect class="photo-cable" x="203" y="273" width="423" height="570" role="img" aria-label="Photo of a pink flat cable with cream connector on a soft pink chevron background"/>

    <g class="brand-band">
      <rect x="203" y="843" width="423" height="75"/>
      <text class="brand" x="414" y="895" text-anchor="middle">MAROBEL</text>
    </g>

    <g class="dot-grid">
      <circle class="dot-white" cx="282" cy="990" r="44"/><circle class="dot-accent" cx="420" cy="990" r="44"/><circle class="dot-white" cx="552" cy="990" r="44"/>
      <circle class="dot-white" cx="282" cy="1110" r="44"/><circle class="dot-accent" cx="420" cy="1110" r="44"/><circle class="dot-white" cx="552" cy="1110" r="44"/>
      <circle class="dot-white" cx="282" cy="1222" r="44"/><circle class="dot-accent" cx="420" cy="1222" r="44"/><circle class="dot-white" cx="552" cy="1222" r="44"/>
      <circle class="dot-white" cx="282" cy="1343" r="44"/><circle class="dot-accent" cx="420" cy="1343" r="44"/><circle class="dot-white" cx="552" cy="1343" r="44"/>
      <circle class="dot-white" cx="282" cy="1457" r="44"/><circle class="dot-accent" cx="420" cy="1457" r="44"/><circle class="dot-white" cx="552" cy="1457" r="44"/>
      <circle class="dot-white" cx="282" cy="1577" r="44"/><circle class="dot-accent" cx="420" cy="1577" r="44"/><circle class="dot-white" cx="552" cy="1577" r="44"/>
    </g>

    <g class="copy copy-front">
      <text x="216" y="1682">Câble compatible pour Vextra 5/6</text>
      <text x="216" y="1726">Recharge rapidement</text>
      <text x="216" y="1770">Toujours à portée de la main</text>
    </g>
  </g>

  <!-- right side panel with tucks -->
  <g class="side-right">
    <path class="panel" d="M647 218 V130 Q647 118 659 118 H791 Q803 118 803 130 V218 L828 242 V1808 L803 1830 V1950 Q803 1962 791 1962 H659 Q647 1962 647 1950 V1830 L627 1808 V272 L647 218 Z"/>
    <line class="fold" x1="627" y1="272" x2="828" y2="272"/>
    <line class="fold" x1="627" y1="1808" x2="828" y2="1808"/>
    <g class="copy copy-side">
      <text transform="translate(752 552) rotate(-90)">Câble compatible pour Vextra 5/6</text>
      <text transform="translate(780 552) rotate(-90)">Recharge rapidement</text>
      <text transform="translate(807 552) rotate(-90)">Toujours à portée de la main</text>
    </g>
    <g class="swatches">
      <circle cx="794" cy="1540" r="15" fill="var(--swatch-orange)"/>
      <circle cx="794" cy="1588" r="15" fill="var(--swatch-pink)"/>
      <circle cx="794" cy="1637" r="15" fill="var(--swatch-green)"/>
      <circle cx="794" cy="1686" r="15" fill="var(--swatch-white)"/>
      <circle cx="794" cy="1733" r="15" fill="var(--swatch-black)"/>
      <circle cx="794" cy="1781" r="15" fill="var(--swatch-blue)"/>
    </g>
    <text class="copy copy-tiny" transform="translate(766 1792) rotate(-90)">Available Colors</text>
  </g>

  <!-- back panel with hang tab -->
  <g class="back">
    <path class="panel" d="M828 242 V102 Q828 72 858 72 H1222 Q1252 72 1252 102 V242 Z"/>
    <path class="fold" d="M962 168 H1005 Q1005 133 1040 133 Q1075 133 1075 168 H1118 A22 22 0 0 1 1118 212 H962 A22 22 0 0 1 962 168 Z"/>
    <rect class="panel" x="828" y="242" width="424" height="1566"/>

    <g class="dot-grid">
      <circle class="dot-white" cx="901" cy="318" r="44"/><circle class="dot-white" cx="1037" cy="318" r="44"/><circle class="dot-white" cx="1169" cy="318" r="44"/>
      <circle class="dot-white" cx="901" cy="440" r="44"/><circle class="dot-white" cx="1037" cy="440" r="44"/><circle class="dot-white" cx="1169" cy="440" r="44"/>
      <circle class="dot-white" cx="903" cy="561" r="44"/><circle class="dot-white" cx="1039" cy="561" r="44"/><circle class="dot-white" cx="1171" cy="561" r="44"/>
      <circle class="dot-accent" cx="901" cy="690" r="44"/><circle class="dot-accent" cx="1037" cy="690" r="44"/><circle class="dot-accent" cx="1169" cy="690" r="44"/>
      <circle class="dot-white" cx="903" cy="812" r="44"/><circle class="dot-white" cx="1039" cy="812" r="44"/><circle class="dot-white" cx="1171" cy="812" r="44"/>
      <circle class="dot-white" cx="905" cy="940" r="44"/><circle class="dot-white" cx="1041" cy="940" r="44"/><circle class="dot-white" cx="1173" cy="940" r="44"/>
      <circle class="dot-white" cx="907" cy="1060" r="44"/><circle class="dot-white" cx="1043" cy="1060" r="44"/><circle class="dot-white" cx="1175" cy="1060" r="44"/>
    </g>

    <g class="brand-band">
      <rect x="829" y="1127" width="422" height="78"/>
      <text class="brand" x="1040" y="1181" text-anchor="middle">MAROBEL</text>
    </g>

    <rect class="photo-keychains" x="829" y="1205" width="422" height="602" role="img" aria-label="Photo of six keychain cables in orange, pink, green, white, black and blue hanging from a key ring on a stone surface"/>
  </g>

  <!-- glue flap -->
  <path class="panel glue-flap" d="M1252 272 L1384 292 V1788 L1252 1808 Z"/>
</svg>
</body>
</html>
```